Faith Based Film Production Ecommerce Site Needed

We are a faith based film production company that offers coaching services as well as physical and digital products.

We have a Wordpress site on Hostwren. It currently, features a landing page (https://brightlampstudio.net/), however we now need a fully fleshed out interactive website that will feature short videos/trailers as well the ability for customers to make online purchases.

The updated site will feature 5 tabs - Take 1, Take 2, Take 3, BTS and Contact. This toolbar/menu should remain fixed/stable while visitors navigate the different tabs/pages, as shown here - https://pelmarokane.com/ (note this site is JUST a reference for its unmoving menu/toolbar in the top right corner of the page).

The text for each tab and actual video content will be provided for potential candidates. Until then, please improvise.

There will be 5 short trailers/reels featured under the "Take 2" tab, that will be shown as thumbnails the same size found here - https://pelmarokane.com/see-pel-at-work/ (reference for thumbnail size only). The names of these trailers will be called, Lamp Summons, Lamp Flourish, Lamp Dawn, Lamp Hearth, and Lamp Courtship.

Lastly, when arriving onto the page, visitors will be greeted with a inaudible video loop, similar to the one found here - https://www.tq-moviehouse.com/ (Note - this is a reference simply to show inaudible video looping). The ACTUAL video to be used however can be found here - https://clipvaultr.net/manage/videos/473918265, beginning at the 15 second mark when the 3 people are entering the cinema and ending at the 28 second mark where the screen gradually fades to black. The video will then consistently re-loop.

Once again, more detail will be provided for the most interesting submissions and of course, official winner.

Should you have any questions until then, please do not hesitate to reach out.

```html
<!DOCTYPE html>
<html lang="en">
<head>
<meta charset="utf-8">
<title>Bright Lamp Studio</title>
<link href="https://fonts.googleapis.com/css2?family=Limelight&family=Kumbh+Sans:wght@400;500;600&display=swap" rel="stylesheet">
<style>
:root{
  --ink:#111111;
  --nav:#121214;
  --white:#ffffff;
  --paper:#f7f7f7;
  --field:#ffffff;
  --muted:#9a9a9a;
  --ghost:#e9e9e9;
  --dark:#262523;
  --dark-2:#1d1c1b;
  --card:#1c1b1a;
  --line:#3a3a3a;
}
*{box-sizing:border-box;margin:0;padding:0}
html,body{width:1200px;height:3245px;overflow:hidden}
body{position:relative;background:var(--white);font-family:"Kumbh Sans",sans-serif;color:var(--ink)}
.abs{position:absolute}
.display{font-family:"Limelight",serif;letter-spacing:1px}

/* header */
.site-header{left:0;top:0;width:1200px;height:63px;background:var(--nav);z-index:5}
.brand{left:164px;top:12px;color:var(--white);font-size:30px;line-height:38px}
.main-nav{right:163px;top:22px;display:flex;gap:36px}
.main-nav a{color:var(--white);text-decoration:none;font-size:13px}

/* hero */
.hero-media{left:0;top:63px;width:1200px;height:561px;background:radial-gradient(ellipse at 55% 55%,#3a3550 0%,#1c2040 45%,#0c1128 100%)}
.play-big{left:559px;top:583px}

/* section headings */
.heading{left:0;width:1200px;text-align:center;font-size:32px}
.heading-rule{height:2px;background:var(--ink)}
.ghost-vertical{font-family:"Limelight",serif;color:var(--ghost);font-size:44px;transform:rotate(-90deg);transform-origin:left top;white-space:nowrap}

/* about */
.about-art{left:239px;top:778px;width:176px;height:305px;background:linear-gradient(180deg,#2a2a2a 0%,#111 70%,#e8e8e8 100%);border-radius:6px}
.about-copy{left:480px;top:804px;width:479px;font-size:13px;line-height:20.7px;text-align:justify;color:#222}
.btn-dark{background:var(--ink);color:var(--white);font-family:"Limelight",serif;font-size:11px;display:flex;align-items:center;justify-content:center;letter-spacing:.5px}

/* take 2 */
.reels-band{left:0;top:1133px;width:1200px;height:752px}
.reel{border-radius:50% 50% 0 0 / 36px 36px 0 0;overflow:hidden}
.reel-play{position:absolute;left:50%;top:50%;width:34px;height:34px;margin:-17px 0 0 -17px;border-radius:50%;background:rgba(30,30,30,.8)}
.reel-play::after{content:"";position:absolute;left:13px;top:10px;border-left:11px solid #fff;border-top:7px solid transparent;border-bottom:7px solid transparent}
.reel-label{height:46px;background:var(--white);font-family:"Limelight",serif;font-size:11px;display:flex;align-items:center;justify-content:center;box-shadow:0 2px 6px rgba(0,0,0,.06);letter-spacing:.5px}
.reel-label.is-active{background:var(--ink);color:var(--white)}

/* services */
.services-band{left:0;top:1885px;width:1200px;height:458px;background:linear-gradient(180deg,var(--dark) 0%,#2b2a27 50%,var(--dark-2) 100%)}
.service{width:207px;height:237px;background:var(--card);color:var(--white);text-align:center}
.service svg{position:absolute;left:72px;top:20px}
.service h3{position:absolute;left:0;top:100px;width:100%;font-family:"Limelight",serif;font-weight:400;font-size:11.5px;letter-spacing:.4px}
.service .rule{position:absolute;left:40px;top:126px;width:127px;height:1px;background:var(--white)}
.service p{position:absolute;left:12px;top:142px;width:183px;font-size:11.6px;line-height:20px}

/* contact */
.field{background:var(--field);box-shadow:0 2px 10px rgba(0,0,0,.07);font-size:11.5px;color:var(--muted);padding:12px 13px}

/* footer */
.site-footer{left:0;top:2920px;width:1200px;height:325px;background:linear-gradient(180deg,#1a1a1a,#232220)}
.foot-brand{left:215px;top:3076px;color:var(--white);font-size:25px}
.social{width:24px;height:24px;border:1.5px solid var(--white);border-radius:50%;top:3114px}
.foot-col h4{color:var(--white);font-size:15px;font-weight:600}
.foot-col .rule{width:93px;height:2px;background:var(--white);margin-top:10px;margin-bottom:10px}
.foot-col a{display:block;color:var(--white);text-decoration:none;font-size:12.5px;line-height:22px}
.foot-contact{color:var(--white);font-size:12.5px;line-height:22px}
.foot-contact svg{position:absolute;left:0}
.foot-contact span{position:absolute;left:28px;white-space:nowrap}
.foot-rule{left:149px;top:3160px;width:892px;height:1px;background:#6a6a6a}
.copyright{left:0;top:3181px;width:1200px;text-align:center;color:var(--white);font-size:12px}
</style>
</head>
<body>

<header class="abs site-header">
  <div class="abs brand display">BRIGHT LAMP</div>
  <nav class="abs main-nav">
    <a href="#">Home</a><a href="#">Take 1</a><a href="#">Take 2</a><a href="#">Take 3</a><a href="#">BTS</a><a href="#">Contact</a>
  </nav>
</header>

<div class="abs hero-media" role="img" aria-label="Looping video still of three friends sharing popcorn in a dim cinema"></div>
<svg class="abs play-big" width="82" height="82" viewBox="0 0 82 82">
  <circle cx="41" cy="41" r="40" fill="none" stroke="#333" stroke-width="1.4" stroke-dasharray="5 4"/>
  <circle cx="41" cy="41" r="31" fill="#fff" style="filter:drop-shadow(0 2px 4px rgba(0,0,0,.25))"/>
  <path d="M35 32 L50 41 L35 50 Z" fill="#111"/>
</svg>

<!-- about -->
<h2 class="abs heading display" style="top:690px">ABOUT THE BRIGHT LAMP</h2>
<div class="abs heading-rule" style="left:499px;top:744px;width:201px"></div>
<div class="abs ghost-vertical" style="left:1108px;top:1022px">ABOUT US</div>
<div class="abs about-art" role="img" aria-label="Black director's chair illustration"></div>
<p class="abs about-copy">Lorem ipsum dolor sit amet, consectetur adipiscing elit, sed do eiusmod tempor incididunt ut labore et dolore magna aliqua. Quis ipsum suspendisse ultrices gravida. Risus commodo viverra maecenas accumsan lacus vel facilisis. omnis iste natus error sit voluptatem accusantium doloremque laudantium, totam rem aperiam, eaque ipsa quae ab illo inventore veritatis et quasi architecto beatae vitae dicta sunt explicabo. Nemo enim ipsam voluptatem quia voluptas sit aspernatur aut odit aut fugit, sed quia consequuntur magni dolores eos qui ratione voluptatem sequi nesciunt. Neque porro quisquam est, qui dolorem ipsum quia dolor sit amet, consectetur, adipisci velit, sed quia non numquam eius modi tempora incidunt ut labore et dolore magnam.</p>
<div class="abs btn-dark" style="left:480px;top:1027px;width:132px;height:38px">ABOUT US</div>

<!-- take 2 -->
<svg class="abs reels-band" width="1200" height="752" viewBox="0 0 1200 752">
  <path d="M0 60 Q600 -60 1200 60 L1200 752 L0 752 Z" fill="#f7f7f7"/>
</svg>
<div class="abs ghost-vertical" style="left:44px;top:1602px">TAKE 2</div>
<h2 class="abs heading display" style="top:1216px">TAKE 2</h2>
<div class="abs heading-rule" style="left:550px;top:1268px;width:101px"></div>

<div class="abs reel" style="left:162px;top:1299px;width:282px;height:206px;background:linear-gradient(160deg,#2c3346,#1a2030 60%,#3b3a44)" role="img" aria-label="Woman smiling at her phone in an office"><span class="reel-play"></span></div>
<div class="abs reel" style="left:458px;top:1299px;width:282px;height:206px;background:linear-gradient(160deg,#f4f2e8,#e6e4d2 50%,#9fb06a)" role="img" aria-label="White orchid blossoms"><span class="reel-play"></span></div>
<div class="abs reel" style="left:754px;top:1299px;width:282px;height:206px;background:linear-gradient(170deg,#cfd8d0,#b49583 55%,#8d5d4b)" role="img" aria-label="Two hands resting together"><span class="reel-play"></span></div>
<div class="abs reel-label" style="left:220px;top:1486px;width:167px">LAMP SUMMONS</div>
<div class="abs reel-label is-active" style="left:516px;top:1486px;width:167px">LAMP FLOURISH</div>
<div class="abs reel-label" style="left:812px;top:1486px;width:167px">LAMP DAWN</div>

<div class="abs reel" style="left:311px;top:1561px;width:282px;height:207px;background:linear-gradient(180deg,#c9d3da,#b5c4cc 55%,#d8d2c6)" role="img" aria-label="Bright living room with blue sofa"><span class="reel-play"></span></div>
<div class="abs reel" style="left:607px;top:1561px;width:282px;height:207px;background:linear-gradient(180deg,#f0c88a,#d89a58 55%,#6a4a3a)" role="img" aria-label="Couple embracing at sunset by the water"><span class="reel-play"></span></div>
<div class="abs reel-label" style="left:368px;top:1746px;width:168px">LAMP HEARTH</div>
<div class="abs reel-label" style="left:664px;top:1746px;width:168px">LAMP COURTSHIP</div>

<!-- what we do -->
<div class="abs services-band"></div>
<div class="abs ghost-vertical" style="left:1110px;top:2290px;color:#35332f">WHAT WE DO</div>
<h2 class="abs heading display" style="top:1950px;color:var(--white)">WHAT WE DO</h2>
<div class="abs heading-rule" style="left:497px;top:2002px;width:206px;background:var(--white)"></div>

<div class="abs service" style="left:162px;top:2032px">
  <svg width="64" height="64" viewBox="0 0 64 64" fill="none" stroke="#fff" stroke-width="2"><rect x="10" y="10" width="36" height="46" rx="2"/><rect x="20" y="6" width="16" height="8" rx="1"/><path d="M16 24h4M24 24h14M16 33h4M24 33h14M16 42h4M24 42h10"/><circle cx="48" cy="18" r="8"/><path d="M44 18l3 3 5-6"/></svg>
  <h3>PROJECT DEVELOPMENT</h3><div class="rule"></div>
  <p>Lorem ipsum dolor sit amet, consectetur adipiscing elit, sed do eiusmod tempor incididunt ut labore et dolore magna.</p>
</div>
<div class="abs service" style="left:385px;top:2032px">
  <svg width="64" height="64" viewBox="0 0 64 64" fill="none" stroke="#fff" stroke-width="2"><path d="M8 12h42v44H8z"/><path d="M14 12v44M14 24h12v16h16M26 40v10M34 30h10"/><path d="M40 22l12-12 4 4-12 12h-4z"/></svg>
  <h3>PRE-PRODUCTION</h3><div class="rule"></div>
  <p>Lorem ipsum dolor sit amet, consectetur adipiscing elit, sed do eiusmod tempor incididunt ut labore et dolore magna.</p>
</div>
<div class="abs service" style="left:608px;top:2032px">
  <svg width="64" height="64" viewBox="0 0 64 64" fill="none" stroke="#fff" stroke-width="2"><path d="M6 18l38-6 1 6-38 6z"/><path d="M7 24h38v26H7z"/><circle cx="20" cy="37" r="7"/><path d="M18 34l5 3-5 3z"/><rect x="32" y="34" width="18" height="16" rx="2"/><path d="M50 38l8-4v16l-8-4"/><circle cx="37" cy="54" r="3"/><circle cx="46" cy="54" r="3"/></svg>
  <h3>PRODUCTION</h3><div class="rule"></div>
  <p>Lorem ipsum dolor sit amet, consectetur adipiscing elit, sed do eiusmod tempor incididunt ut labore et dolore magna.</p>
</div>
<div class="abs service" style="left:831px;top:2032px">
  <svg width="64" height="64" viewBox="0 0 64 64" fill="none" stroke="#fff" stroke-width="2"><rect x="4" y="8" width="56" height="26"/><path d="M4 14h56M4 28h56M12 8v6M20 8v6M44 8v6M52 8v6M12 28v6M52 28v6"/><path d="M28 17l7 4-7 4z"/><circle cx="22" cy="52" r="6"/><circle cx="42" cy="52" r="6"/><path d="M26 47l14-16M38 47L24 31"/></svg>
  <h3>POST-PRODUCTION</h3><div class="rule"></div>
  <p>Lorem ipsum dolor sit amet, consectetur adipiscing elit, sed do eiusmod tempor incididunt ut labore et dolore magna.</p>
</div>

<!-- contact -->
<h2 class="abs heading display" style="top:2420px">CONTACT US</h2>
<div class="abs heading-rule" style="left:550px;top:2473px;width:101px"></div>
<div class="abs field" style="left:219px;top:2518px;width:373px;height:38px">First Name</div>
<div class="abs field" style="left:607px;top:2518px;width:373px;height:38px">Last Name</div>
<div class="abs field" style="left:219px;top:2580px;width:373px;height:39px">Email Address</div>
<div class="abs field" style="left:607px;top:2580px;width:373px;height:39px">Phone Number</div>
<div class="abs field" style="left:219px;top:2643px;width:761px;height:128px">Message</div>
<div class="abs btn-dark" style="left:534px;top:2806px;width:132px;height:38px">SUBMIT NOW</div>

<!-- footer -->
<footer class="abs site-footer"></footer>
<div class="abs foot-brand display">BRIGHT LAMP</div>
<div class="abs social" style="left:238px"></div>
<div class="abs social" style="left:274px"></div>
<div class="abs social" style="left:309px"></div>
<div class="abs social" style="left:344px"></div>

<div class="abs foot-col" style="left:490px;top:2978px">
  <h4>QUICK LINKS</h4><div class="rule"></div>
  <a href="#">Home</a><a href="#">Take 1</a><a href="#">Take 2</a><a href="#">Take 3</a><a href="#">BTS</a>
</div>
<div class="abs foot-col" style="left:664px;top:2978px">
  <h4>OTHER LINKS</h4><div class="rule"></div>
  <a href="#">Terms &amp; conditions</a><a href="#">Privacy Policy</a><a href="#">Contact</a><a href="#">FAQ</a>
</div>
<div class="abs foot-col" style="left:843px;top:2978px">
  <h4>CONTACT US</h4><div class="rule"></div>
</div>
<div class="abs foot-contact" style="left:846px;top:3023px;width:240px;height:130px">
  <svg style="top:6px" width="12" height="14" viewBox="0 0 12 14"><path d="M6 0a5 5 0 0 1 5 5c0 4-5 9-5 9S1 9 1 5a5 5 0 0 1 5-5z" fill="#fff"/><circle cx="6" cy="5" r="2" fill="#1d1d1d"/></svg>
  <span style="top:0">123 Lorem ipsum dolor sit amet,</span>
  <span style="top:22px">consectetur adipiscing</span>
  <svg style="top:61px" width="13" height="10" viewBox="0 0 13 10"><rect width="13" height="10" fill="#fff"/><path d="M0 0l6.5 5L13 0" fill="none" stroke="#1d1d1d" stroke-width="1.3"/></svg>
  <span style="top:55px">hello@brightlampstudio.net</span>
  <svg style="top:101px" width="12" height="12" viewBox="0 0 12 12"><path d="M2 0l3 3-1.5 2a8 8 0 0 0 3.5 3.5L9 7l3 3-2 2C5 12 0 7 0 2z" fill="#fff"/></svg>
  <span style="top:97px">555-014-2290</span>
</div>
<div class="abs foot-rule"></div>
<div class="abs copyright">© 2023 Bright Lamp Studio &nbsp;&nbsp;&nbsp;&nbsp;|&nbsp;&nbsp;&nbsp;&nbsp; All rights reserved.</div>

</body>
</html>
```